brightcover.com.au website design

We need a website design for a new Australian company called brightcover.com.au As the name suggests we provide life insurance quotes for consumers on line. When people contact us we can provide various policy and product options to suit their needs whatever they may be.
Our service is all about simplifying life insurance, taking the worry, stress and guesswork out of obtaining the right life insurance.
Life insurance is a cyclical business triggered predominantly by key events in an individuals life, namely taking out a mortgage, starting a family, a health scare either relating to themselves or a friend or more increasingly a natural disaster which highlights the fragility of life.
We want the brightcover.com.au brand to be viewed as honest and reliable as well as being innovative and modern.

Target Market(s)

Primary audience - Young Mid Life Families with the Mother being the primary decision maker for the family budget.

Industry/Entity Type

Life Insurance

```html
<!DOCTYPE html>
<html lang="en">
<head>
<meta charset="utf-8">
<title>brightcover.com.au — Life Insurance Quotes</title>
<link rel="stylesheet" href="https://fonts.googleapis.com/css2?family=Montserrat:ital,wght@0,300;0,400;0,500;1,300&family=PT+Sans:wght@400&family=Arimo:wght@400;700&display=swap">
<style>
  :root {
    --teal: #1b9bb5;
    --teal-dark: #106f8f;
    --teal-deep: #0e5f80;
    --teal-light: #2fb4c9;
    --crimson: #b0114f;
    --crimson-dark: #8a0a3c;
    --orange: #f07a1a;
    --ink: #2f3336;
    --grey-bg: #e8ebee;
    --grey-text: #6b6f72;
    --white: #ffffff;
    --social-blue: #1f3a93;
    --social-sky: #2fc0e8;
  }
  * { margin: 0; padding: 0; box-sizing: border-box; }
  html, body { width: 1200px; height: 768px; overflow: hidden; background: var(--white); }
  body { position: relative; font-family: "Montserrat", sans-serif; color: var(--ink); }

  /* Header */
  .site-header { position: absolute; top: 0; left: 0; width: 1200px; height: 48px; background: var(--white); }
  .brand { position: absolute; left: 118px; top: 11px; font-family: "Montserrat", sans-serif; font-weight: 500; font-size: 23px; color: var(--teal); letter-spacing: 0.5px; text-transform: uppercase; }
  .main-nav { position: absolute; top: 19px; left: 0; width: 1200px; font-size: 13px; letter-spacing: 0.6px; }
  .main-nav a { position: absolute; color: var(--ink); text-decoration: none; white-space: nowrap; }
  .main-nav a.is-current { color: var(--crimson); }
  .nav-caret { display: inline-block; width: 0; height: 0; margin-left: 7px; vertical-align: 1px; border-left: 5px solid transparent; border-right: 5px solid transparent; border-top: 8px solid var(--orange); }

  /* Tagline band */
  .tagline-band { position: absolute; top: 48px; left: 0; width: 1200px; height: 90px;
    background: linear-gradient(90deg, var(--teal-deep) 0%, var(--teal) 45%, var(--teal) 70%, var(--teal-dark) 100%); }
  .tagline { position: absolute; left: 118px; top: 26px; font-weight: 300; font-size: 30px; color: var(--white); letter-spacing: 0.6px; white-space: nowrap; }
  .tagline em { font-style: italic; }
  .btn-start { position: absolute; left: 918px; top: 28px; width: 162px; height: 38px; background: linear-gradient(#ffffff, #e6e6e6); border-radius: 5px; box-shadow: 0 1px 3px rgba(0,0,0,0.3); }
  .btn-start span { position: absolute; left: 11px; top: 9px; font-size: 18px; color: var(--ink); }
  .btn-start .divider { position: absolute; left: 130px; top: 0; width: 1px; height: 38px; background: #cfcfcf; }
  .btn-start svg { position: absolute; left: 141px; top: 11px; }

  /* Hero */
  .hero { position: absolute; top: 138px; left: 0; width: 1200px; height: 334px; background: var(--grey-bg); overflow: hidden; }
  .hero-photo { position: absolute; left: 270px; top: 0; width: 830px; height: 334px;
    background: radial-gradient(ellipse at 60% 50%, #8d8d8d 0%, #b3b3b3 40%, rgba(232,235,238,0) 75%); }
  .hero-title { position: absolute; left: 124px; top: 63px; font-weight: 300; font-size: 34px; line-height: 35px; color: var(--ink); letter-spacing: 1px; }
  .hero-sub { position: absolute; left: 126px; top: 135px; font-style: italic; font-weight: 300; font-size: 22px; color: var(--orange); letter-spacing: 0.4px; }
  .btn-quote { position: absolute; left: 115px; top: 209px; width: 396px; height: 63px; border-radius: 3px;
    background: linear-gradient(var(--crimson), var(--crimson-dark)); box-shadow: 0 1px 3px rgba(0,0,0,0.35); }
  .btn-quote .divider { position: absolute; left: 55px; top: 0; width: 1px; height: 63px; background: rgba(0,0,0,0.25); }
  .btn-quote svg { position: absolute; left: 21px; top: 16px; }
  .btn-quote span { position: absolute; left: 68px; top: 19px; font-size: 19px; color: var(--white); letter-spacing: 0.4px; white-space: nowrap; }

  /* Products */
  .products { position: absolute; top: 474px; left: 0; width: 1200px; height: 215px;
    background: radial-gradient(ellipse at 55% 80%, var(--teal-light) 0%, var(--teal) 45%, var(--teal-dark) 100%); }
  .products-bar { position: absolute; top: 0; left: 0; width: 1200px; height: 52px; background: rgba(10,70,110,0.45); border-bottom: 1px solid rgba(255,255,255,0.25); }
  .product { position: absolute; top: 0; width: 240px; }
  .product-head { position: absolute; top: 10px; left: 0; height: 34px; display: flex; align-items: center; gap: 8px; white-space: nowrap; font-size: 19px; color: var(--white); letter-spacing: 0.3px; }
  .product-text { position: absolute; top: 64px; left: 0; width: 230px; font-family: "PT Sans", sans-serif; font-size: 14px; line-height: 24px; color: var(--white); letter-spacing: 0.2px; }

  /* Footer */
  .site-footer { position: absolute; top: 689px; left: 0; width: 1200px; height: 79px; background: var(--white); font-family: "Arimo", sans-serif; }
  .footer-nav a { position: absolute; top: 16px; font-size: 13px; color: var(--grey-text); text-decoration: none; }
  .copyright { position: absolute; left: 105px; top: 48px; font-size: 11px; font-weight: 700; color: #9a9da0; }
  .social { position: absolute; top: 13px; font-family: "Montserrat", sans-serif; font-weight: 500; font-size: 15px; }
  .social.circlebook { left: 883px; color: var(--social-blue); }
  .social.chatterly { left: 993px; color: var(--social-sky); }
</style>
</head>
<body>

<header class="site-header">
  <div class="brand">brightcover.com.au</div>
  <nav class="main-nav">
    <a class="is-current" style="left:450px">HOME</a>
    <a style="left:530px">PERSONAL RISK PRODUCTS<span class="nav-caret"></span></a>
    <a style="left:758px">MEDIA</a>
    <a style="left:842px">TESTIMONIALS</a>
    <a style="left:986px">CONTACT US</a>
  </nav>
</header>

<section class="tagline-band">
  <p class="tagline"><em>Because</em> life insurance shouldn’t be overwhelming.</p>
  <a class="btn-start">
    <span>Get Started</span>
    <i class="divider"></i>
    <svg width="10" height="16" viewBox="0 0 10 16"><path d="M0 0 L10 8 L0 16 Z" fill="var(--crimson)"/></svg>
  </a>
</section>

<section class="hero">
  <div class="hero-photo" role="img" aria-label="Black and white photo of a pregnant mother walking hand in hand with her young daughter past an old building"></div>
  <h1 class="hero-title" style="font-weight:300">Your time should be<br>spent with your family</h1>
  <p class="hero-sub">… not worrying about insurance.</p>
  <a class="btn-quote">
    <svg width="16" height="30" viewBox="0 0 16 30"><path d="M0 0 L16 15 L0 30 Z" fill="var(--white)"/></svg>
    <i class="divider"></i>
    <span>Start your Life Insurance quote</span>
  </a>
</section>

<section class="products">
  <div class="products-bar"></div>

  <article class="product" style="left:119px">
    <h2 class="product-head" style="font-weight:400">
      <svg width="40" height="34" viewBox="0 0 40 34" fill="var(--orange)">
        <circle cx="9" cy="4" r="3.5"/><path d="M3 9 h12 l-2 11 h-2 v14 h-4 v-14 h-2 z"/>
        <circle cx="27" cy="4" r="3.5"/><path d="M22 9 h10 v12 h-2 v13 h-6 v-13 h-2 z"/>
      </svg>
      Life Insurance
    </h2>
    <p class="product-text">Life Insurance is an agreed cash sum payable upon death. Designed to protect family and home.</p>
  </article>

  <article class="product" style="left:359px">
    <h2 class="product-head" style="font-weight:400">
      <svg width="32" height="32" viewBox="0 0 32 32">
        <circle cx="16" cy="16" r="13.5" fill="none" stroke="var(--orange)" stroke-width="3"/>
        <text x="16" y="23" text-anchor="middle" font-family="Arimo, sans-serif" font-weight="700" font-size="19" fill="var(--orange)">$</text>
      </svg>
      Income Protection
    </h2>
    <p class="product-text">Income Protection provides up to 75% of your income if you are unable to work due to illness or injury.</p>
  </article>

  <article class="product" style="left:619px">
    <h2 class="product-head" style="font-weight:400">
      <svg width="44" height="30" viewBox="0 0 44 30" fill="var(--orange)">
        <rect x="2" y="3" width="30" height="3"/><rect x="16" y="6" width="3" height="4"/>
        <path d="M6 10 h22 a8 8 0 0 1 8 8 v2 h-30 z"/><rect x="30" y="14" width="12" height="3"/>
        <rect x="8" y="24" width="24" height="2.5"/><rect x="12" y="20" width="2" height="5"/><rect x="26" y="20" width="2" height="5"/>
      </svg>
      Trauma Cover
    </h2>
    <p class="product-text">Trauma Cover is an agreed cash sum payable upon suffering a traumatic medical event.</p>
  </article>

  <article class="product" style="left:851px">
    <h2 class="product-head" style="font-weight:400">
      <svg width="30" height="34" viewBox="0 0 30 34">
        <circle cx="10" cy="4" r="3.5" fill="var(--orange)"/>
        <path d="M10 9 v12 h10 l5 9" fill="none" stroke="var(--orange)" stroke-width="3.5" stroke-linecap="round" stroke-linejoin="round"/>
        <path d="M6 15 a10 10 0 1 0 14 12" fill="none" stroke="var(--orange)" stroke-width="3"/>
      </svg>
      T&amp;P Disablement
    </h2>
    <p class="product-text">Term &amp; Permanent Disablement is an agreed cash sum is payable upon permanent disablement.</p>
  </article>
</section>

<footer class="site-footer">
  <nav class="footer-nav">
    <a style="left:110px">Home</a>
    <a style="left:181px">Personal Risk Products</a>
    <a style="left:352px">Media</a>
    <a style="left:424px">Testimonials</a>
  </nav>
  <p class="copyright">© 2011 brightcover.com.au. All Rights Reserved</p>
  <a class="social circlebook">circlebook</a>
  <a class="social chatterly">chatterly</a>
</footer>

</body>
</html>
```